Corvallin Property Solutions need a business card design

Hello guys. We would need a business card design asap please.
We are a start up property investment business based in London UK specialised in buying, selling, managing and letting properties and helping distressed property owners.
The name of our Business is Corvallin, the logo symbolises the four fundamental elements of the world (earth, air, fire and water) and so it stands for strength, stability, longevity.
We would like the business card to communicate professionalism and reliability. Many many thanks indeed for your work.

Details:

1.) Marisol Dunkley
Property Investor
Mobile: +44(0)7700362517
Email: marisol.corvallin@quilbrook.example

2.) Tomas Brindle
Property Investor
Mobile: +44(0)7700845926
Email: tomas.corvallin@quilbrook.example

Industry/Entity Type

Investment

```html
<!DOCTYPE html>
<html lang="en">
<head>
<meta charset="utf-8">
<title>Corvallin Property Solutions — Business Card</title>
<link rel="stylesheet" href="https://fonts.googleapis.com/css2?family=Open+Sans:wght@400;600;700&display=swap">
<style>
  :root {
    --page: #e9e6e1;
    --card-dark: #1f1f21;
    --card-dark-edge: #2c2c2f;
    --card-light: #ffffff;
    --ink-light: #f2f2f2;
    --ink-grey: #8a8a8a;
    --ink-dark: #3a3a3a;
    --brand-red: #d62a36;
    --brand-blue: #3f6fc4;
    --brand-green: #2a9a4a;
  }
  * { box-sizing: border-box; margin: 0; padding: 0; }
  html, body {
    width: 704px; height: 1200px; overflow: hidden;
    background: var(--page);
    font-family: "Open Sans", Arial, sans-serif;
  }
  .canvas {
    width: 704px; height: 1200px;
    display: flex; flex-direction: column;
    align-items: center; justify-content: space-around;
    padding: 60px 0;
  }
  .card {
    position: relative;
    width: 580px; height: 340px;
    border-radius: 22px;
    overflow: hidden;
    box-shadow: 0 10px 28px rgba(0,0,0,.22);
  }
  .card--front {
    background: linear-gradient(160deg, var(--card-dark-edge) 0%, var(--card-dark) 60%);
  }
  .card--back { background: var(--card-light); }

  .edge-bands {
    position: absolute; top: 0; right: 0; bottom: 0; width: 24px;
    display: flex; flex-direction: column;
  }
  .edge-bands span { flex: 1; }
  .band--red { background: var(--brand-red); }
  .band--blue { background: var(--brand-blue); }
  .band--green { background: var(--brand-green); }

  .brand {
    position: absolute;
    display: flex; align-items: center; gap: 18px;
  }
  .brand__square { width: 46px; height: 46px; }
  .brand__name {
    font-weight: 700; letter-spacing: 2px; line-height: 1.15;
    text-transform: uppercase;
  }
  .card--front .brand { left: 110px; top: 128px; }
  .card--front .brand__square { background: var(--ink-light); }
  .card--front .brand__name { color: var(--ink-light); font-size: 34px; }
  .brand__name small { display: block; font-size: 15px; letter-spacing: 3px; }

  .card--back .brand { left: 40px; bottom: 44px; }
  .card--back .brand__square { background: var(--ink-grey); width: 38px; height: 38px; }
  .card--back .brand__name { color: var(--ink-grey); font-size: 26px; }
  .card--back .brand__name small { font-size: 12px; }

  .contact {
    position: absolute; right: 56px; top: 44px;
    text-align: right;
  }
  .contact__name { color: var(--brand-red); font-size: 22px; font-weight: 400; }
  .contact__role { color: var(--brand-blue); font-size: 15px; margin-top: 2px; }
  .contact__lines { margin-top: 26px; color: var(--ink-dark); font-size: 14px; }
  .contact__line {
    display: flex; align-items: center; justify-content: flex-end; gap: 8px;
    margin-top: 6px;
  }
  .contact__line svg { width: 14px; height: 14px; }
</style>
</head>
<body>
<main class="canvas">
  <section class="card card--front" aria-label="Card front">
    <div class="brand">
      <span class="brand__square"></span>
      <p class="brand__name">Corvallin<small>Property Solutions</small></p>
    </div>
    <div class="edge-bands">
      <span class="band--red"></span>
      <span class="band--blue"></span>
      <span class="band--green"></span>
    </div>
  </section>

  <section class="card card--back" aria-label="Card back">
    <div class="contact">
      <p class="contact__name">Marisol Dunkley</p>
      <p class="contact__role">Property Investor</p>
      <div class="contact__lines">
        <p class="contact__line">+44(0)7700362517
          <svg viewBox="0 0 14 14" aria-hidden="true"><rect x="3.5" y="1" width="7" height="12" rx="1.5" fill="none" stroke="var(--brand-green)" stroke-width="1.4"/><circle cx="7" cy="10.8" r=".8" fill="var(--brand-green)"/></svg>
        </p>
        <p class="contact__line">marisol.corvallin@quilbrook.example
          <svg viewBox="0 0 14 14" aria-hidden="true"><rect x="1" y="3" width="12" height="8" fill="var(--brand-green)"/><path d="M1 3 L7 8 L13 3" fill="none" stroke="#fff" stroke-width="1"/></svg>
        </p>
      </div>
    </div>
    <div class="brand">
      <span class="brand__square"></span>
      <p class="brand__name">Corvallin<small>Property Solutions</small></p>
    </div>
    <div class="edge-bands">
      <span class="band--green"></span>
      <span class="band--red"></span>
      <span class="band--blue"></span>
    </div>
  </section>
</main>
</body>
</html>
```